Stationery Design Project

We need a stationery design for our Norwegian trucking company. We have existed for about 15 years and our 12 drivers uses relatively new vehicles to transport goods around in northern Norway. Long distance routes with fresh fish og food transport is our main operations.

We have already made alogo that's printed on our trucks. The logo and a picture of our trucks is attached. I think the logo i crappy, but since its already in use, changing it is not an option in this round. Still using a better colour scheme in the overall stationery and more interesting fonts is possible (altso in the logo).

Company details:
Name: Vikmarka AS
Organisation nr 983 517 608
Post adress: 8640 Brekka

I like minimalism and simplicity. I am avalibly for questions in normal GMT working hours either here or on mail: kjell@brekkafrakt.no

Reason: Hi. Im extending the deadline because I needed some time to find a vector file of our logo. Sorry for the inconvenience

Hi, and thanks for all your interest in the project. Some updates:

-          I have decided to commit to using one of the designs. Some designer will get the payment.

-          I have extended the deadline with 24 hours since I needed some time to find our firms vector logo (a slow Swedish man was holding me up)

-          We will not choose a design before the deadline. No need to rush.

-          We have received a lot of great design and think there is a need to specified the product we want to make:

o   Business Card for all our employers. I just need the design and will duplicate with the correct numbers and name myself. The information on should be: Logo, employer’s name, Phone number, email, website, Postal number and address. Use this as a template: logo, Leif Dahlberg, 47382950, Leif@brekkafrakt.no,, brekkafrakt.no, 8640 Brekka. The order and placement of the information is your creative decision.

o   Stickers to put on the goods we travel. On the sticker the should be the following information: Logo, phone number, Tekst and link: Fraktæ av Vikmarka. Ke du syns? Brekkafrakt.no/tilbakemelding (this means: Handled by Vikmarka. What do you think Brekkafrakt.no/feedback -à the link will be a feedback form). The placement the information and size is your creative decision with some stings: we have been thinking of using Prentolo for printing and see that a size about 6x6 cm, 8x5 or something like that. (with 3000 copies our budget is 200 punds). Any suggestions of other suppliers are welcome. Prentolo price calculator http://www.prentoloprints.example/digital-litho-printing/printing-labels-tags/stickers/

o   Letterhead with logo, address, phone number and organizational number.

o   Envelopes with logo,address, phone number and organizational number.

Have a nice day.

 

 

• Using the blue colour in the logo and using a similar graphic approch.

```html
<!DOCTYPE html>
<html lang="no">
<head>
<meta charset="utf-8">
<title>Vikmarka AS – Stationery</title>
<link href="https://fonts.googleapis.com/css2?family=Arimo:wght@400;700&display=swap" rel="stylesheet">
<style>
  :root {
    --brand-blue: #0a4fae;
    --brand-blue-dark: #063a8a;
    --brand-blue-light: #2a7fd4;
    --paper: #ffffff;
    --backdrop: #e6e7e9;
    --ink: #3a3a3a;
    --shadow: 0 2px 6px rgba(0,0,0,.12);
  }
  * { box-sizing: border-box; margin: 0; padding: 0; }
  html, body { width: 1200px; height: 800px; overflow: hidden; }
  body {
    background: var(--backdrop);
    font-family: "Arimo", Arial, sans-serif;
    color: var(--ink);
    position: relative;
  }
  .sheet { position: absolute; background: var(--paper); box-shadow: var(--shadow); overflow: hidden; }
  .sheet > svg.swoosh { position: absolute; inset: 0; width: 100%; height: 100%; }

  .brand { display: inline-flex; align-items: center; gap: 6px; font-weight: 700; color: var(--brand-blue); }
  .brand-dot { width: .7em; height: .7em; border-radius: 50%; background: currentColor; }

  .label { color: var(--brand-blue-light); }

  /* Business card – back */
  .card-back {
    left: 40px; top: 60px; width: 255px; height: 160px;
    background: linear-gradient(135deg, var(--brand-blue-light), var(--brand-blue-dark));
    display: flex; flex-direction: column; align-items: center; justify-content: center; gap: 22px;
  }
  .card-back .brand { color: var(--paper); font-size: 28px; }
  .card-back .card-web { color: #cfe0f7; font-size: 7px; letter-spacing: .5px; }

  /* Business card – front */
  .card-front { left: 320px; top: 60px; width: 255px; height: 160px; }
  .card-front .brand { position: absolute; left: 16px; top: 16px; font-size: 18px; }
  .card-front .card-details { position: absolute; left: 16px; top: 58px; font-size: 7px; line-height: 1.45; }
  .card-front .card-name { color: var(--brand-blue); font-weight: 700; font-size: 11px; margin-bottom: 3px; }

  /* Stickers */
  .sticker {
    position: absolute; width: 230px; height: 124px; border-radius: 50%;
    background: var(--paper); border: 3px solid var(--brand-blue);
    box-shadow: var(--shadow); overflow: hidden;
  }
  .sticker > svg.swoosh { position: absolute; inset: 0; width: 100%; height: 100%; }
  .sticker .brand { position: absolute; left: 34px; top: 24px; font-size: 22px; }
  .sticker .sticker-text { position: absolute; left: 40px; top: 58px; font-size: 7.5px; line-height: 1.45; }
  .sticker .sticker-text strong { color: var(--brand-blue); }
  .sticker-a { left: 40px; top: 258px; }
  .sticker-b { left: 300px; top: 258px; }

  /* Envelope */
  .envelope { left: 40px; top: 420px; width: 580px; height: 300px; }
  .envelope .brand { position: absolute; left: 26px; top: 26px; font-size: 24px; }
  .envelope .sender { position: absolute; left: 28px; top: 64px; font-size: 8px; line-height: 1.45; }
  .envelope .sender strong { color: var(--brand-blue); }

  /* Letterhead */
  .letterhead { left: 650px; top: 40px; width: 510px; height: 720px; }
  .letter-head { position: absolute; left: 44px; right: 40px; top: 36px; display: flex; justify-content: space-between; align-items: flex-end; }
  .letter-head .brand { font-size: 30px; }
  .letter-head .contact { font-size: 7.5px; line-height: 1.45; }
  .letter-head .contact strong { color: var(--brand-blue); font-size: 9px; }
  .letter-body { position: absolute; left: 44px; right: 44px; top: 116px; font-size: 7.6px; line-height: 1.55; text-align: justify; }
  .letter-body p { margin-bottom: 12px; }
</style>
</head>
<body>

  <!-- Business card back -->
  <section class="sheet card-back">
    <span class="brand"><span class="brand-dot"></span>Vikmarka</span>
    <span class="card-web">www.brekkafrakt.no</span>
  </section>

  <!-- Business card front -->
  <section class="sheet card-front">
    <svg class="swoosh" viewBox="0 0 255 160" preserveAspectRatio="none" aria-hidden="true">
      <path d="M150 160 Q230 120 255 30 L255 160 Z" fill="var(--brand-blue)"/>
      <path d="M185 160 Q240 110 255 70 L255 160 Z" fill="var(--brand-blue-light)"/>
      <path d="M120 160 Q215 130 245 40 Q225 125 140 160 Z" fill="var(--brand-blue-dark)"/>
    </svg>
    <span class="brand"><span class="brand-dot"></span>Vikmarka</span>
    <div class="card-details">
      <div class="card-name">Leif Dahlberg</div>
      <div>8640 Brekka</div>
      <div><span class="label">phone:</span> 47382950</div>
      <div><span class="label">email:</span> Leif@brekkafrakt.no</div>
      <div><span class="label">web:</span> brekkafrakt.no</div>
    </div>
  </section>

  <!-- Stickers -->
  <section class="sticker sticker-a">
    <svg class="swoosh" viewBox="0 0 230 124" preserveAspectRatio="none" aria-hidden="true">
      <path d="M110 124 Q200 110 230 50 L230 124 Z" fill="var(--brand-blue)"/>
      <path d="M150 124 Q215 100 230 75 L230 124 Z" fill="var(--brand-blue-light)"/>
    </svg>
    <span class="brand"><span class="brand-dot"></span>Vikmarka</span>
    <div class="sticker-text">
      <strong>Fraktæ av Vikmarka. Ke du syns?</strong><br>
      Brekkafrakt.no/tilbakemelding<br>
      <span class="label">phone:</span> 75624830
    </div>
  </section>
  <section class="sticker sticker-b">
    <svg class="swoosh" viewBox="0 0 230 124" preserveAspectRatio="none" aria-hidden="true">
      <path d="M110 124 Q200 110 230 50 L230 124 Z" fill="var(--brand-blue)"/>
      <path d="M150 124 Q215 100 230 75 L230 124 Z" fill="var(--brand-blue-light)"/>
    </svg>
    <span class="brand"><span class="brand-dot"></span>Vikmarka</span>
    <div class="sticker-text">
      <strong>Fraktæ av Vikmarka. Ke du syns?</strong><br>
      Brekkafrakt.no/tilbakemelding<br>
      <span class="label">phone:</span> 75624830
    </div>
  </section>

  <!-- Envelope -->
  <section class="sheet envelope">
    <svg class="swoosh" viewBox="0 0 580 300" preserveAspectRatio="none" aria-hidden="true">
      <path d="M300 300 Q520 250 580 110 L580 300 Z" fill="var(--brand-blue)"/>
      <path d="M380 300 Q540 240 580 170 L580 300 Z" fill="var(--brand-blue-light)"/>
      <path d="M240 300 Q500 270 565 100 Q530 250 290 300 Z" fill="var(--brand-blue-dark)"/>
      <path d="M440 300 Q560 250 580 210 L580 300 Z" fill="var(--brand-blue-dark)"/>
    </svg>
    <span class="brand"><span class="brand-dot"></span>Vikmarka</span>
    <div class="sender">
      <strong>8640 Brekka</strong><br>
      <span class="label">phone:</span> 75624830 &nbsp;<span class="label">organization:</span> 983 517 608
    </div>
  </section>

  <!-- Letterhead -->
  <section class="sheet letterhead">
    <svg class="swoosh" viewBox="0 0 510 720" preserveAspectRatio="none" aria-hidden="true">
      <path d="M0 500 Q40 640 510 650 L510 720 L0 720 Z" fill="var(--brand-blue)"/>
      <path d="M0 560 Q80 680 510 690 L510 720 L0 720 Z" fill="var(--brand-blue-light)"/>
      <path d="M0 470 Q30 620 380 660 Q60 640 0 530 Z" fill="var(--brand-blue-dark)"/>
      <path d="M0 620 Q140 710 510 705 L510 720 L0 720 Z" fill="var(--brand-blue-dark)"/>
    </svg>
    <header class="letter-head">
      <span class="brand"><span class="brand-dot"></span>Vikmarka</span>
      <div class="contact">
        <strong>8640 Brekka</strong><br>
        <span class="label">phone:</span> 75624830 &nbsp;<span class="label">organization:</span> 983 517 608<br>
        <span class="label">web:</span> www.brekkafrakt.no
      </div>
    </header>
    <div class="letter-body">
      <p>Dear Client,</p>
      <p>Lorem ipsum dolor sit amet, consectetur adipisicing elit, sed do eiusmod tempor incididunt ut labore et dolore magna aliqua. Ut enim ad minim veniam, quis nostrud exercitation ullamco laboris nisi ut aliquip ex ea commodo consequat. Duis aute irure dolor in reprehenderit in voluptate velit esse cillum dolore eu fugiat nulla pariatur. Excepteur sint occaecat cupidatat non proident, sunt in culpa qui officia deserunt mollit anim id est laborum.</p>
      <p>Lorem ipsum dolor sit amet, consectetur adipisicing elit, sed do eiusmod tempor incididunt ut labore et dolore magna aliqua. Ut enim ad minim veniam, quis nostrud exercitation ullamco laboris nisi ut aliquip ex ea commodo consequat. Duis aute irure dolor in reprehenderit in voluptate velit esse cillum dolore eu fugiat nulla pariatur. Excepteur sint occaecat cupidatat non proident, sunt in culpa qui officia deserunt mollit anim id est laborum.</p>
      <p>Lorem ipsum dolor sit amet, consectetur adipisicing elit, sed do eiusmod tempor incididunt ut labore et dolore magna aliqua. Ut enim ad minim veniam, quis nostrud exercitation ullamco laboris nisi ut aliquip ex ea commodo consequat. Duis aute irure dolor in reprehenderit in voluptate velit esse cillum dolore eu fugiat nulla pariatur. Excepteur sint occaecat cupidatat non proident, sunt in culpa qui officia deserunt mollit anim id est laborum.</p>
      <p>Lorem ipsum dolor sit amet, consectetur adipisicing elit, sed do eiusmod tempor incididunt ut labore et dolore magna aliqua. Ut enim ad minim veniam, quis nostrud exercitation ullamco laboris nisi ut aliquip ex ea commodo consequat. Duis aute irure dolor in reprehenderit in voluptate velit esse cillum dolore eu fugiat nulla pariatur. Excepteur sint occaecat cupidatat non proident, sunt in culpa qui officia deserunt mollit anim id est laborum.</p>
      <p>Lorem ipsum dolor sit amet, consectetur adipisicing elit, sed do eiusmod tempor incididunt ut labore et dolore magna aliqua. Ut enim ad minim veniam, quis nostrud exercitation ullamco laboris nisi ut aliquip ex ea commodo consequat. Duis aute irure dolor in reprehenderit in voluptate velit esse cillum dolore eu fugiat nulla pariatur. Excepteur sint occaecat cupidatat non proident, sunt in culpa qui officia deserunt mollit anim id est laborum.</p>
    </div>
  </section>

</body>
</html>
```